Verdon Ridgeworks Ltd. - Refreshed business card challenge

A revised, refreshed business card design for my oil and gas company using my existing logo. Feel free to be as creative as you like!

Target Market(s)

bankers, lawyers

Industry/Entity Type

Oil And Gas Exploration

Contact Information for Business Card

See the "Must Haves" section

Font styles to use
Serif
Sans Serif

Colors

Designer to choose colors to be used in the design.

Requirements
Must have
• Existing business logo, name, title, email, phone number, business address
• Neil Hastow, CA, CPA
• Vice President Finance & Chief Financial Officer
• nhastow@verdonridgeworks.example
• office: (555)284-6071
• cell: (555)716-3342
• 840, 615 11 Street N.E.
• Calgary, AB
• X9Q 4K1
Should not have
• Should not be plain and boring.

```html
<!DOCTYPE html>
<html lang="en">
<head>
<meta charset="utf-8">
<title>Verdon Ridgeworks – Business Card</title>
<link rel="stylesheet" href="https://fonts.googleapis.com/css2?family=Exo+2:wght@400;500;600;800&display=swap">
<style>
  :root {
    --stage: #3a3a3c;
    --forest: #0b4d32;
    --forest-deep: #083f29;
    --paper: #ffffff;
    --bark: #4a2812;
    --mist: #d9dcd8;
    --mist-warm: #e2d8d2;
  }
  * { box-sizing: border-box; margin: 0; padding: 0; }
  html, body {
    width: 1200px; height: 900px; overflow: hidden;
    background: var(--stage);
    font-family: "Exo 2", sans-serif;
  }
  .card {
    position: absolute; left: 290px;
    width: 620px; height: 354px;
    overflow: hidden;
  }
  /* Front */
  .card-front { top: 48px; background: var(--forest); }
  .front-tree {
    position: absolute; left: 232px; top: 34px;
    width: 66px; height: 290px;
    background: linear-gradient(180deg, rgba(255,255,255,.85), rgba(255,255,255,.95));
    border-radius: 30px 30px 6px 6px;
  }
  .front-name {
    position: absolute; left: 300px; top: 232px;
    color: var(--paper); font-weight: 800;
    font-size: 38px; line-height: 1; letter-spacing: -.5px;
  }
  /* Back */
  .card-back { top: 448px; background: var(--paper); }
  .back-tree {
    position: absolute; left: 478px; top: 70px;
    width: 70px; height: 262px;
    background: linear-gradient(180deg, var(--mist), var(--mist-warm));
    border-radius: 30px 30px 6px 6px;
    opacity: .8;
  }
  .back-logo {
    position: absolute; right: 28px; top: 34px;
    color: var(--forest); font-weight: 800;
    font-size: 30px; line-height: 1; letter-spacing: -.5px;
  }
  .holder { position: absolute; left: 40px; top: 40px; }
  .holder-name {
    color: var(--bark); font-weight: 600; font-size: 32px; line-height: 1;
  }
  .holder-name .credentials {
    font-size: 16px; font-weight: 500; color: var(--forest-deep); margin-left: 10px;
  }
  .holder-title {
    margin-top: 6px; color: var(--forest-deep); font-size: 16px; font-weight: 500;
  }
  .contacts { list-style: none; margin-top: 12px; }
  .contacts li {
    display: flex; align-items: center; gap: 10px;
    color: var(--bark); font-size: 17px; height: 28px;
  }
  .contacts svg { width: 18px; height: 18px; fill: var(--forest); flex: none; }
  .address {
    position: absolute; right: 28px; bottom: 38px;
    color: var(--forest-deep); font-size: 17px; font-weight: 500;
  }
  .base-band {
    position: absolute; left: 0; right: 0; bottom: 0; height: 22px;
    background: var(--forest);
  }
</style>
</head>
<body>
  <section class="card card-front">
    <div class="front-tree" role="img" aria-label="White silhouette of a tall spruce tree with small firs at its base"></div>
    <div class="front-name">Verdon Ridgeworks</div>
  </section>

  <section class="card card-back">
    <div class="back-tree" role="img" aria-label="Faint grey silhouette of a tall spruce tree"></div>
    <div class="back-logo">Verdon Ridgeworks</div>

    <div class="holder">
      <h1 class="holder-name">Neil Hastow<span class="credentials">CA, CPA</span></h1>
      <p class="holder-title">Vice President Finance &amp; Chief Financial Officer</p>
      <ul class="contacts">
        <li>
          <svg viewBox="0 0 24 24" aria-hidden="true"><path d="M3 8c0-2 2-3 9-3s9 1 9 3v2h-5V8H8v2H3zM6 11h12l2 9H4zm6 2a3 3 0 1 0 0 6 3 3 0 0 0 0-6z"/></svg>
          (555)284-6071
        </li>
        <li>
          <svg viewBox="0 0 24 24" aria-hidden="true"><path d="M7 2h10a2 2 0 0 1 2 2v16a2 2 0 0 1-2 2H7a2 2 0 0 1-2-2V4a2 2 0 0 1 2-2zm0 3v13h10V5zm5 14.2a1 1 0 1 0 0 2 1 1 0 0 0 0-2z"/></svg>
          (555)716-3342
        </li>
        <li>
          <svg viewBox="0 0 24 24" aria-hidden="true"><path d="M2 5h20v14H2zm2 2v.5l8 5.5 8-5.5V7zm0 3v7h16v-7l-8 5.5z"/></svg>
          nhastow@verdonridgeworks.example
        </li>
        <li>
          <svg viewBox="0 0 24 24" aria-hidden="true"><path d="M12 2a10 10 0 1 0 0 20 10 10 0 0 0 0-20zm-1 2.1V8H7.6A8 8 0 0 1 11 4.1zm2 0A8 8 0 0 1 16.4 8H13zM5.1 10H11v3H4.1a8 8 0 0 1 1-3zM13 10h5.9a8 8 0 0 1 1 3H13zM4.3 15H11v4.9A8 8 0 0 1 4.3 15zM13 15h6.7a8 8 0 0 1-6.7 4.9z"/></svg>
          www.verdonridgeworks.example
        </li>
      </ul>
    </div>

    <p class="address">840, 615 11 Street N.E. Calgary, AB, X9Q 4K1</p>
    <div class="base-band"></div>
  </section>
</body>
</html>
```